The Festival! Poster for an Annual Dance Showcase

We are looking for a dynamic festival/concert style poster for our annual dance showcase featuring at least one image of our dancers and the main information. The main image should be one of the dancers but there can be a collage of the dancers or smaller images around the poster. I have included some reference images but it can vary from them.

Must have this information;
Date - May 22-26
Location - Mabel Corwin Hale Theatre
Tickets - Vondo.bm

Target Market(s)

Parents and people who love dance

Industry/Entity Type

Dance

Font styles to use
Sans Serif

Colors
E54698
E96AAD
F1A4CE
F9D9EA
FCEFF6

Requirements
Must have
• Logo, Date and Location, Picture of Dancer

```html
<!DOCTYPE html>
<html lang="en">
<head>
<meta charset="utf-8">
<title>Dance Showcase – Step Forward School of Dance</title>
<link rel="stylesheet" href="https://fonts.googleapis.com/css2?family=Poppins:wght@500;600;700&display=swap">
<style>
  :root {
    --magenta-deep: #c21f8f;
    --magenta: #d93aa8;
    --pink-hot: #e54698;
    --pink: #e96aad;
    --pink-soft: #f1a4ce;
    --lilac: #dc7fe0;
    --blush: #f9d9ea;
    --cream: #fbeae0;
    --ink: #b5208a;
  }
  * { margin: 0; padding: 0; box-sizing: border-box; }
  html, body { width: 800px; height: 1200px; overflow: hidden; background: var(--pink); }
  .poster {
    position: relative;
    width: 800px;
    height: 1200px;
    overflow: hidden;
    font-family: "Poppins", sans-serif;
    background: linear-gradient(160deg, var(--pink-hot) 0%, var(--lilac) 45%, var(--magenta) 100%);
  }
  .waves { position: absolute; inset: 0; width: 800px; height: 1200px; }

  .brand {
    position: absolute;
    left: 40px;
    top: 46px;
    display: flex;
    align-items: center;
    gap: 14px;
    color: var(--cream);
    font-weight: 600;
    line-height: 1.05;
  }
  .brand-dot { width: 44px; height: 44px; border-radius: 50%; background: var(--cream); }
  .brand-name { font-size: 30px; letter-spacing: 0.5px; }
  .brand-name span { display: block; font-size: 22px; letter-spacing: 1px; }

  .dancer {
    position: absolute;
    border-radius: 48% 52% 45% 55% / 40% 45% 55% 60%;
  }
  .dancer-leap { left: 300px; top: 60px; width: 390px; height: 360px;
    background: radial-gradient(ellipse at 55% 50%, #b8229a 0%, rgba(184,34,154,0.55) 60%, rgba(184,34,154,0) 75%); }
  .dancer-ballet { left: 86px; top: 180px; width: 195px; height: 320px;
    background: radial-gradient(ellipse at 50% 45%, #f07ac0 0%, rgba(240,122,192,0.5) 60%, rgba(240,122,192,0) 78%); }
  .dancer-reach { left: 620px; top: 455px; width: 140px; height: 155px;
    background: radial-gradient(ellipse at 50% 50%, #e27ed3 0%, rgba(226,126,211,0.4) 60%, rgba(226,126,211,0) 78%); }
  .dancer-pose { left: 20px; top: 690px; width: 260px; height: 435px;
    background: radial-gradient(ellipse at 50% 50%, #e0206f 0%, rgba(224,32,111,0.55) 60%, rgba(224,32,111,0) 78%); }

  .title {
    position: absolute;
    left: 0;
    width: 800px;
    top: 440px;
    text-align: center;
    color: var(--cream);
    font-weight: 600;
    font-size: 136px;
    line-height: 116px;
    letter-spacing: 1px;
  }
  .title span { display: block; }

  .pill {
    position: absolute;
    left: 353px;
    width: 320px;
    background: var(--cream);
    color: var(--ink);
    border-radius: 40px;
    display: flex;
    align-items: center;
    justify-content: center;
    font-weight: 700;
  }
  .date { top: 715px; height: 74px; font-size: 44px; letter-spacing: 0.5px; }
  .venue {
    position: absolute;
    left: 320px;
    width: 386px;
    top: 812px;
    text-align: center;
    color: var(--ink);
    font-weight: 700;
    font-size: 38px;
    line-height: 42px;
    letter-spacing: 0.5px;
  }
  .venue span { display: block; }
  .tickets { top: 924px; height: 66px; font-size: 28px; letter-spacing: 0.5px; }
</style>
</head>
<body>
<main class="poster">
  <svg class="waves" viewBox="0 0 800 1200" aria-hidden="true">
    <path d="M0 120 C150 60 260 200 420 150 S650 60 800 110 V0 H0Z" fill="#ef5fb8"/>
    <path d="M0 260 C160 200 300 330 470 270 S680 170 800 220 V330 C660 300 540 400 380 370 S130 300 0 360Z" fill="#f28bd1" opacity="0.7"/>
    <path d="M0 420 C180 360 320 500 500 440 S700 360 800 400 V520 C650 490 520 590 360 560 S120 490 0 540Z" fill="#e04cb8" opacity="0.55"/>
    <path d="M0 640 C170 590 310 720 490 660 S700 580 800 620 V740 C640 710 520 820 350 780 S110 710 0 760Z" fill="#f47ac6" opacity="0.55"/>
    <path d="M0 860 C190 810 330 930 500 880 S710 800 800 840 V960 C650 930 520 1030 360 1000 S130 930 0 980Z" fill="#de8ae0" opacity="0.6"/>
    <path d="M0 1060 C170 1010 320 1140 500 1080 S700 1010 800 1050 V1200 H0Z" fill="#d22f9e" opacity="0.75"/>
  </svg>

  <header class="brand">
    <div class="brand-dot"></div>
    <div class="brand-name">STEP FORWARD<span>SCHOOL OF DANCE</span></div>
  </header>

  <div class="dancer dancer-leap" role="img" aria-label="Silhouette of a dancer in a grand leap"></div>
  <div class="dancer dancer-ballet" role="img" aria-label="Silhouette of a ballerina with one leg raised high"></div>
  <div class="dancer dancer-reach" role="img" aria-label="Faint silhouette of a dancer reaching upward"></div>
  <div class="dancer dancer-pose" role="img" aria-label="Silhouette of a dancer posing with arms extended"></div>

  <h1 class="title"><span>DANCE</span><span>SHOWCASE</span></h1>

  <p class="pill date">MAY 22-26</p>
  <p class="venue"><span>MABEL CORWIN</span><span>HALE THEATRE</span></p>
  <p class="pill tickets">TICKETS: VONDO.BM</p>
</main>
</body>
</html>
```